Gobal construction supply company needs new business card design

I need a business card design for my global supply company using an existing logo. i will be looking to print these on rounded corner cards with the black background version of my logo on the back. on the front white background, my logo again and my simple details.

```html
<!DOCTYPE html>
<html lang="en">
<head>
<meta charset="utf-8">
<title>Meridian Build Supply – Business Cards</title>
<link rel="stylesheet" href="https://fonts.googleapis.com/css2?family=Montserrat:wght@600;700&family=Work+Sans:wght@400;500&display=swap">
<style>
  :root {
    --stage: #1f2327;
    --card-black: #231f20;
    --card-white: #ffffff;
    --brand-red: #d71f26;
    --ink: #231f20;
    --map-tone: #3a3637;
  }
  * { box-sizing: border-box; margin: 0; padding: 0; }
  html, body { width: 1200px; height: 738px; overflow: hidden; }
  body {
    background: var(--stage);
    position: relative;
    font-family: "Work Sans", Arial, sans-serif;
  }
  .card {
    position: absolute;
    top: 220px;
    width: 520px;
    height: 297px;
    border-radius: 14px;
    overflow: hidden;
  }
  .card--back { left: 50px; background: var(--card-black); }
  .card--front { left: 630px; background: var(--card-white); }

  .world-map {
    position: absolute;
    left: 40px; top: 30px;
    width: 440px; height: 237px;
    border-radius: 40px;
    background: radial-gradient(ellipse at center, var(--map-tone) 0%, rgba(58,54,55,0.4) 55%, rgba(35,31,32,0) 80%);
  }
  .brand {
    display: flex;
    align-items: center;
    gap: 8px;
    font-family: "Montserrat", Arial, sans-serif;
    font-weight: 700;
    letter-spacing: 0.5px;
    white-space: nowrap;
  }
  .brand__square { display: block; background: var(--brand-red); }

  .card--back .brand {
    position: absolute;
    left: 0; right: 0; top: 128px;
    justify-content: center;
    color: #fff;
    font-size: 22px;
  }
  .card--back .brand__square { width: 16px; height: 16px; }
  .card--back .rule {
    position: absolute;
    left: 130px; right: 130px; top: 170px;
    height: 2px;
    background: var(--brand-red);
  }

  .card--front .brand {
    position: absolute;
    left: 28px; top: 48px;
    color: var(--ink);
    font-size: 15px;
  }
  .card--front .brand__square { width: 11px; height: 11px; }
  .card--front .brand-rule {
    position: absolute;
    left: 28px; top: 76px;
    width: 200px; height: 1.5px;
    background: var(--brand-red);
  }
  .person {
    position: absolute;
    right: 30px; top: 40px;
    text-align: right;
  }
  .person__name {
    font-family: "Montserrat", Arial, sans-serif;
    font-weight: 600;
    font-size: 18px;
    color: var(--brand-red);
    letter-spacing: 0.3px;
  }
  .person__title { font-size: 12px; color: var(--ink); margin-top: 1px; }
  .divider {
    position: absolute;
    left: 28px; right: 30px; top: 96px;
    height: 1px;
    background: var(--brand-red);
    opacity: 0.7;
  }
  .contact {
    position: absolute;
    left: 30px; top: 124px;
    list-style: none;
    font-size: 13px;
    color: var(--ink);
    line-height: 17px;
    letter-spacing: 0.4px;
  }
  .contact li { display: flex; align-items: center; gap: 8px; }
  .contact svg { width: 9px; height: 9px; flex: none; fill: none; stroke: var(--brand-red); stroke-width: 1.6; }
  .contact .accent { color: var(--brand-red); }
  .wave { position: absolute; left: 0; bottom: 0; width: 520px; height: 160px; }
  .address {
    position: absolute;
    right: 28px; top: 216px;
    color: #fff;
    font-size: 12.5px;
    line-height: 17px;
    text-align: left;
    letter-spacing: 0.4px;
  }
</style>
</head>
<body>
  <section class="card card--back" aria-label="Card back">
    <div class="world-map" role="img" aria-label="Faint dotted world map in the background"></div>
    <div class="brand"><span class="brand__square"></span>MERIDIAN BUILD SUPPLY</div>
    <div class="rule"></div>
  </section>

  <section class="card card--front" aria-label="Card front">
    <div class="brand"><span class="brand__square"></span>MERIDIAN BUILD SUPPLY</div>
    <div class="brand-rule"></div>

    <div class="person">
      <p class="person__name">DANIEL HART</p>
      <p class="person__title">Director</p>
    </div>
    <div class="divider"></div>

    <ul class="contact">
      <li><svg viewBox="0 0 10 10"><path d="M2 1 L4 3 L3 4 Q5 7 6 7 L7 6 L9 8 L8 9 Q3 9 1 2 Z"/></svg><span>555-010-2468</span></li>
      <li><svg viewBox="0 0 10 10"><rect x="1" y="2" width="8" height="6"/><path d="M1 2 L5 5.5 L9 2"/></svg><span>info@meridianbuild.com</span></li>
      <li><svg viewBox="0 0 10 10"><circle cx="5" cy="5" r="4"/><path d="M1 5 H9 M5 1 Q2.5 5 5 9 M5 1 Q7.5 5 5 9"/></svg><span>www.<span class="accent">meridianbuild</span>.com</span></li>
    </ul>

    <svg class="wave" viewBox="0 0 520 160" preserveAspectRatio="none" aria-hidden="true">
      <path d="M0 80 Q120 120 260 60 Q380 10 520 20 L520 160 L0 160 Z" fill="var(--brand-red)"/>
      <path d="M0 112 Q140 138 280 82 Q400 36 520 32 L520 160 L0 160 Z" fill="var(--card-white)"/>
      <path d="M0 118 Q140 144 280 88 Q400 42 520 38 L520 160 L0 160 Z" fill="var(--card-black)"/>
    </svg>
    <p class="address">48 Harbour Road Box<br>902, Lakeview, AB</p>
  </section>
</body>
</html>
```